Medical VIP club - small design

Please read the specs in a design brief attached. Also we don't have logo in a Vector format and attaching the only version we have.

Industry/Entity Type

Club

```html
<!DOCTYPE html>
<html lang="en">
<head>
<meta charset="utf-8">
<title>Curavia – VIP Club</title>
<link href="https://fonts.googleapis.com/css2?family=Libre+Baskerville:ital,wght@0,700;1,700&family=Questrial&display=swap" rel="stylesheet">
<style>
  :root {
    --page-bg: #b6afa6;
    --band-brown: #6e5446;
    --tile-band: #8b6c5e;
    --nav-dark: #4a3a36;
    --nav-light: #7a6963;
    --ink-dark: #1e1512;
    --logo-brown: #6a4b40;
    --footer-bg: #2e2220;
    --footer-text: #d8cfc8;
    --white: #ffffff;
    --dot-active: #c9967a;
    --slide-warm-1: #3b2a1a;
    --slide-warm-2: #b27a2c;
    --slide-warm-3: #e8c27a;
  }
  * { box-sizing: border-box; margin: 0; padding: 0; }
  html, body { width: 1200px; height: 843px; overflow: hidden; }
  body {
    position: relative;
    background: var(--page-bg);
    font-family: "Questrial", sans-serif;
  }
  .brand {
    position: absolute; left: 62px; top: 48px;
    display: flex; align-items: center; gap: 12px;
  }
  .brand-dot { width: 30px; height: 30px; border-radius: 50%; background: var(--logo-brown); }
  .brand-name {
    font-family: "Libre Baskerville", serif; font-weight: 700;
    font-size: 50px; color: var(--logo-brown); letter-spacing: 1px;
  }
  .contact {
    position: absolute; right: 68px; top: 46px; text-align: right;
    font-family: "Libre Baskerville", serif; font-style: italic; font-weight: 700;
    color: var(--ink-dark);
  }
  .contact-label { font-size: 21px; margin-right: 26px; }
  .contact-phone { font-size: 35px; line-height: 44px; }

  .main-nav {
    position: absolute; left: 63px; top: 128px; width: 1074px; height: 44px;
    display: flex;
    background: linear-gradient(var(--nav-light), var(--nav-dark));
    border: 1px solid #8e817b;
  }
  .main-nav a {
    text-decoration: none; color: var(--white);
    font-family: "Libre Baskerville", serif; font-style: italic; font-weight: 700;
    font-size: 20px;
    display: flex; align-items: center; justify-content: center;
    border-right: 1px solid #2e2420; box-shadow: inset -1px 0 #8c7c76;
  }
  .main-nav a:last-child { border-right: none; box-shadow: none; }
  .main-nav a.current { color: var(--ink-dark); background: linear-gradient(#8c7b75, #5d4c47); }

  .slider-band {
    position: absolute; left: 0; top: 172px; width: 1200px; height: 325px;
    background: var(--band-brown);
  }
  .slide {
    position: absolute; left: 63px; top: 172px; width: 1074px; height: 325px;
    background:
      radial-gradient(ellipse at 62% 35%, var(--slide-warm-3) 0%, transparent 45%),
      linear-gradient(90deg, var(--slide-warm-1), var(--slide-warm-2) 45%, #6f7f8c 75%, var(--slide-warm-1));
  }
  .slide-title {
    position: absolute; left: 128px; top: 198px;
    font-family: "Libre Baskerville", serif; font-style: italic; font-weight: 700;
    font-size: 42px; color: var(--ink-dark);
    text-shadow: 0 0 6px rgba(255,255,255,.7);
  }
  .slide-points { position: absolute; left: 128px; top: 262px; list-style: none; }
  .slide-points li {
    display: flex; align-items: center; gap: 14px; height: 34px;
    font-family: "Libre Baskerville", serif; font-style: italic; font-weight: 700;
    font-size: 16px; color: var(--white);
  }
  .arrow { position: absolute; top: 300px; width: 50px; height: 50px; }
  .arrow.prev { left: 40px; }
  .arrow.next { left: 1108px; }
  .slide-dots { position: absolute; left: 998px; top: 456px; display: flex; gap: 3px; }
  .slide-dots span { width: 21px; height: 21px; border-radius: 50%; background: var(--white); }
  .slide-dots span.active { background: var(--dot-active); border: 2px solid var(--white); width: 26px; height: 26px; margin-top: -2px; }

  .tile-band {
    position: absolute; left: 65px; top: 527px; width: 1070px; height: 180px;
    background: var(--tile-band); border-radius: 14px;
  }
  .service-tile {
    position: absolute; top: 516px; height: 198px; border-radius: 14px; overflow: hidden;
    box-shadow: 0 2px 5px rgba(0,0,0,.5);
  }
  .service-tile .photo { position: absolute; inset: 0; }
  .service-tile .caption {
    position: absolute; left: 0; right: 0; bottom: 0; height: 50px;
    background: rgba(40,30,28,.72); color: var(--white);
    font-size: 17px; letter-spacing: .5px; line-height: 21px;
    display: flex; align-items: center; justify-content: center; text-align: center;
  }
  .tile-doctors { left: 72px; width: 198px; }
  .tile-doctors .photo { background: linear-gradient(#f2f2f2, #9fbccc); }
  .tile-hotel { left: 289px; width: 195px; }
  .tile-hotel .photo { background: linear-gradient(#a88766, #5a3a28); }
  .tile-emergency { left: 502px; width: 195px; }
  .tile-emergency .photo { background: linear-gradient(160deg, #2f3a2c 20%, #e9e6e2 45%, #bdb7b2); }
  .tile-transport { left: 718px; width: 194px; }
  .tile-transport .photo { background: linear-gradient(#3c3c3c, #b9b5b2 60%, #6a6662); }
  .tile-register { left: 932px; width: 195px; }
  .tile-register .photo { background: linear-gradient(135deg, #f4f4f4, #c9c9c9); }

  .site-footer {
    position: absolute; left: 0; top: 741px; width: 1200px; height: 102px;
    background: var(--footer-bg); border-top: 2px dashed #8c8581;
  }
  .footer-nav { position: absolute; left: 65px; top: 30px; display: flex; }
  .footer-nav a { color: var(--footer-text); text-decoration: none; font-size: 12px; font-family: Arial, sans-serif; }
  .copyright {
    position: absolute; left: 66px; top: 66px; color: var(--footer-text);
    font-size: 13px; letter-spacing: .6px;
  }
  .find-us { position: absolute; left: 462px; top: 57px; display: flex; align-items: center; gap: 5px; }
  .find-us-label { color: var(--footer-text); font-size: 17px; font-weight: 700; margin-right: 3px; letter-spacing: .5px; }
  .social { width: 32px; height: 32px; border-radius: 5px; }
  .social.one { background: #3fb2e2; }
  .social.two { background: #3c5fa8; }
  .social.three { background: #e8692c; }
  .footer-brand {
    position: absolute; left: 950px; top: 38px; display: flex; align-items: center; gap: 8px;
  }
  .footer-brand .brand-dot { width: 20px; height: 20px; background: #8e6e62; }
  .footer-brand .brand-name { font-size: 34px; color: #8e6e62; }
</style>
</head>
<body>
  <header>
    <div class="brand"><span class="brand-dot"></span><span class="brand-name">Curavia</span></div>
    <div class="contact">
      <div class="contact-label">Contact Us Now</div>
      <div class="contact-phone">Call : 416-555-0142</div>
    </div>
    <nav class="main-nav">
      <a href="#" style="width:128px">Home</a>
      <a href="#" class="current" style="width:170px">VIP Club</a>
      <a href="#" style="width:214px">Our Services</a>
      <a href="#" style="width:215px">Registration</a>
      <a href="#" style="width:163px">Packeges</a>
      <a href="#" style="width:184px">Contact Us</a>
    </nav>
  </header>

  <section class="hero">
    <div class="slider-band"></div>
    <div class="slide" role="img" aria-label="Photo of a bright hotel lobby with a couple standing at the reception"></div>
    <h1 class="slide-title">VIP Club</h1>
    <ul class="slide-points">
      <li><svg width="28" height="28" viewBox="0 0 24 24"><path d="M12 1l3.2 7 7.6.8-5.7 5.1 1.7 7.5L12 17.6 5.2 21.4l1.7-7.5L1.2 8.8 8.8 8z" fill="#b8aca3"/></svg>Lorem ipsum dolor sit amet, consetetur ....</li>
      <li><svg width="28" height="28" viewBox="0 0 24 24"><path d="M12 1l3.2 7 7.6.8-5.7 5.1 1.7 7.5L12 17.6 5.2 21.4l1.7-7.5L1.2 8.8 8.8 8z" fill="#b8aca3"/></svg>Lorem ipsum dolor sit amet, consetetur ....</li>
      <li><svg width="28" height="28" viewBox="0 0 24 24"><path d="M12 1l3.2 7 7.6.8-5.7 5.1 1.7 7.5L12 17.6 5.2 21.4l1.7-7.5L1.2 8.8 8.8 8z" fill="#b8aca3"/></svg>Lorem ipsum dolor sit amet, consetetur ....</li>
    </ul>
    <svg class="arrow prev" viewBox="0 0 50 50"><circle cx="25" cy="25" r="24" fill="#fff" fill-opacity=".55"/><path d="M29 14L18 25l11 11" stroke="#fff" stroke-width="5" fill="none"/></svg>
    <svg class="arrow next" viewBox="0 0 50 50"><circle cx="25" cy="25" r="24" fill="#fff" fill-opacity=".55"/><path d="M21 14l11 11-11 11" stroke="#fff" stroke-width="5" fill="none"/></svg>
    <div class="slide-dots"><span class="active"></span><span></span><span></span><span></span><span></span></div>
  </section>

  <section class="services">
    <div class="tile-band"></div>
    <a class="service-tile tile-doctors"><div class="photo" role="img" aria-label="Photo of smiling medical staff in scrubs"></div><div class="caption">Variety Experienced<br>Doctors</div></a>
    <a class="service-tile tile-hotel"><div class="photo" role="img" aria-label="Photo of a hotel bedroom"></div><div class="caption">Hotel Services</div></a>
    <a class="service-tile tile-emergency"><div class="photo" role="img" aria-label="Photo of a hospital emergency entrance sign"></div><div class="caption">Emergenct Plans</div></a>
    <a class="service-tile tile-transport"><div class="photo" role="img" aria-label="Photo of an ambulance and a car in a parking garage"></div><div class="caption">Transport</div></a>
    <a class="service-tile tile-register"><div class="photo" role="img" aria-label="Photo of a fountain pen on a contract"></div><div class="caption">Register Here</div></a>
  </section>

  <footer class="site-footer">
    <nav class="footer-nav">
      <a href="#" style="width:70px">Home</a>
      <a href="#" style="width:92px">VIP Club</a>
      <a href="#" style="width:116px">Our Services</a>
      <a href="#" style="width:116px">Registration</a>
      <a href="#" style="width:93px">Packeges</a>
      <a href="#">Contact Us</a>
    </nav>
    <p class="copyright">Copyright © 2011 Curavia. All Right Reserve</p>
    <div class="find-us">
      <span class="find-us-label">Find Us:</span>
      <span class="social one"></span><span class="social two"></span><span class="social three"></span>
    </div>
    <div class="footer-brand"><span class="brand-dot"></span><span class="brand-name">Curavia</span></div>
  </footer>
</body>
</html>
```